Eycatcher Flyer
Zielgruppe
Infos auf www.lumawerk-beratung.ch
Lebensberatung, Seminare, persönliche Weiterbildung,Medium
Aufgabenstellung
Suche ein Design für einen coolen, modernen, mystischen exklusiven(Image) Flyer. Format A4 Längs gefaltet (Endformat A5).
Flyer Titel Liebe dein Leben - Liebe dich selbst eventuell auch auf englisch love yourself and celebrates your life
oder vielleicht hat jemand noch einen besseren Slogan Vorschlag
Habe im Anhang ein Dokument mit Text kann ganz oder auszugweise verwendet werden. (Handelt sich um einen ersten Entwurf mögliche Rechtschreibfehler enthalten)
Ansonsten Inputs aus der Hp holen.
Lieblingsfarben Rot,Pink,Giftgrün,Gold,Schwarz, Gelb,

```html
<!DOCTYPE html>
<html lang="de">
<head>
<meta charset="utf-8">
<title>Lumawerk – Flyer Liebe dein Leben</title>
<link href="https://fonts.googleapis.com/css2?family=Open+Sans:ital,wght@0,400;0,600;1,400;1,600&display=swap" rel="stylesheet">
<style>
  :root{
    --board:#bdbdbd;
    --ink:#000;
    --paper:#fff;
    --pink:#e8146a;
  }
  *{margin:0;padding:0;box-sizing:border-box}
  html,body{width:1200px;height:1111px;overflow:hidden;background:var(--board)}
  body{font-family:'Open Sans',Arial,sans-serif;color:var(--paper);position:relative}
  .panel{position:absolute;background:var(--ink);overflow:hidden;box-shadow:2px 3px 5px rgba(0,0,0,.35)}
  .panel svg.art{position:absolute;inset:0;width:100%;height:100%}
  .single{width:331px;height:468px}
  .spread{width:663px;height:468px}
  .front-single{left:81px;top:65px}
  .cover-spread{left:470px;top:65px}
  .back-single{left:81px;top:561px}
  .inside-spread{left:470px;top:561px}

  .brand{position:absolute;display:flex;align-items:center;gap:7px}
  .brand-dot{width:22px;height:22px;border-radius:50%;background:var(--pink)}
  .brand-name{font-size:19px;font-weight:400;color:var(--paper);letter-spacing:.5px}

  .slogan{position:absolute;text-align:right;white-space:nowrap}
  .slogan-de{font-size:12.6px;font-weight:600;line-height:16px}
  .slogan-en{font-size:11.6px;font-style:italic;color:var(--pink);line-height:15px}

  .contact{position:absolute;font-size:9.6px;font-weight:600;line-height:13px}
  .contact .gap{margin-top:13px}
  .contact .web{color:var(--pink)}

  .column{position:absolute;width:240px;font-size:8.5px;line-height:11.85px}
  .column p{margin-bottom:11.85px}
  .column strong{font-weight:600}
  .accent{color:var(--pink)}
  .inside-title{position:absolute;font-size:18px;font-style:italic;font-weight:600;color:var(--pink)}
  .checklist{list-style:none;margin-bottom:11.85px}
  .checklist li{padding-left:10px;position:relative}
  .checklist li::before{content:"›";position:absolute;left:0;top:-2px;color:var(--pink);font-weight:600;font-size:12px}
  .closing{font-style:italic;font-weight:600;color:var(--pink)}
</style>
</head>
<body>

<svg width="0" height="0" style="position:absolute">
  <defs>
    <linearGradient id="sand" x1="0" y1="0" x2="1" y2="1">
      <stop offset="0" stop-color="#f1eee9"/><stop offset="1" stop-color="#cfc7bb"/>
    </linearGradient>
    <radialGradient id="stone" cx=".5" cy=".5" r=".5">
      <stop offset="0" stop-color="#bdb4a6"/><stop offset="1" stop-color="#a79d8f" stop-opacity="0"/>
    </radialGradient>
    <radialGradient id="bloom" cx=".5" cy=".5" r=".5">
      <stop offset="0" stop-color="#b0127a"/><stop offset=".5" stop-color="#c94fb8"/><stop offset="1" stop-color="#c94fb8" stop-opacity="0"/>
    </radialGradient>
    <linearGradient id="blush" x1="0" y1="0" x2="1" y2="1">
      <stop offset="0" stop-color="#fbe3ef"/><stop offset=".6" stop-color="#e779b9"/><stop offset="1" stop-color="#c0389d"/>
    </linearGradient>
    <radialGradient id="blushRound" cx=".7" cy=".55" r=".6">
      <stop offset="0" stop-color="#e2559f"/><stop offset=".5" stop-color="#f6c6dc"/><stop offset="1" stop-color="#fff"/>
    </radialGradient>
    <linearGradient id="bronze" x1="0" y1="0" x2="1" y2="1">
      <stop offset="0" stop-color="#c38a45"/><stop offset="1" stop-color="#5a3413"/>
    </linearGradient>
    <clipPath id="front-sand-area">
      <path d="M0,246 C110,172 290,138 447,120 L447,600 L100,600 L60,515 C40,510 10,490 0,450 Z"/>
    </clipPath>
    <clipPath id="spread-sand-area">
      <path d="M447,120 C290,138 130,175 40,260 C-20,330 -35,420 -30,470 C-20,520 20,540 60,515 L100,600 L447,600 Z"/>
    </clipPath>
  </defs>
</svg>

<!-- Front cover -->
<section class="panel single front-single">
  <svg class="art" viewBox="0 0 447 632">
    <path class="swoosh" d="M447,35 C420,120 350,142 250,150 C140,160 60,192 0,222 L0,632 L447,632 Z" fill="#fff"/>
    <g class="photo" clip-path="url(#front-sand-area)" role="img" aria-label="Foto: gestapelte Steine im Zen-Sandgarten mit pinker Orchidee">
      <rect x="0" y="100" width="447" height="520" fill="url(#sand)"/>
      <ellipse cx="170" cy="300" rx="110" ry="95" fill="url(#stone)"/>
      <ellipse cx="265" cy="345" rx="95" ry="85" fill="url(#bloom)"/>
    </g>
    <path class="text-blob" d="M58,632 C28,560 40,470 130,432 C210,398 300,420 360,445 C385,428 418,426 418,450 C418,472 388,470 362,462 C400,500 430,522 447,530 L447,632 Z" fill="#000" stroke="#fff" stroke-width="9"/>
  </svg>
  <div class="brand" style="left:41px;top:40px"><span class="brand-dot"></span><span class="brand-name">Lumawerk</span></div>
  <div class="slogan" style="right:47px;top:393px">
    <div class="slogan-de">Liebe dein Leben - Liebe dich selbst</div>
    <div class="slogan-en">love yourself and celebrates your life</div>
  </div>
</section>

<!-- Outer spread: back + cover -->
<section class="panel spread cover-spread">
  <svg class="art" viewBox="0 0 895 632">
    <g class="back-art">
      <path d="M0,0 L195,0 C165,110 90,190 0,238 Z" fill="#fff"/>
      <path d="M0,0 L140,0 C115,85 65,150 0,188 Z" fill="url(#blush)" role="img" aria-label="Foto: pinke Orchidee"/>
    </g>
    <g class="cover-art" transform="translate(448,0)">
      <path class="swoosh" d="M447,35 C420,120 350,142 250,150 C120,165 0,250 -40,380 C-65,470 -45,570 -10,632 L447,632 Z" fill="#fff"/>
      <g class="photo" clip-path="url(#spread-sand-area)" role="img" aria-label="Foto: gestapelte Steine im Zen-Sandgarten mit pinker Orchidee">
        <rect x="-40" y="100" width="487" height="520" fill="url(#sand)"/>
        <ellipse cx="170" cy="300" rx="110" ry="95" fill="url(#stone)"/>
        <ellipse cx="265" cy="345" rx="95" ry="85" fill="url(#bloom)"/>
      </g>
      <path class="text-blob" d="M58,632 C28,560 40,470 130,432 C210,398 300,420 360,445 C385,428 418,426 418,450 C418,472 388,470 362,462 C400,500 430,522 447,530 L447,632 Z" fill="#000" stroke="#fff" stroke-width="9"/>
    </g>
  </svg>
  <div class="brand" style="left:54px;top:258px"><span class="brand-dot"></span><span class="brand-name">Lumawerk</span></div>
  <div class="contact" style="left:53px;top:322px">
    <div>Lumawerk</div><div>8500 Lindenau</div><div>Tel:078 000 12 34</div>
    <div class="gap">info@lumawerk-beratung.ch</div><div class="web">www.lumawerk-beratung.ch</div>
  </div>
  <div class="brand" style="left:373px;top:40px"><span class="brand-dot"></span><span class="brand-name">Lumawerk</span></div>
  <div class="slogan" style="right:47px;top:393px">
    <div class="slogan-de">Liebe dein Leben - Liebe dich selbst</div>
    <div class="slogan-en">love yourself and celebrates your life</div>
  </div>
</section>

<!-- Back panel -->
<section class="panel single back-single">
  <svg class="art" viewBox="0 0 447 632">
    <path d="M0,0 L195,0 C165,110 90,190 0,238 Z" fill="#fff"/>
    <path d="M0,0 L140,0 C115,85 65,150 0,188 Z" fill="url(#blush)" role="img" aria-label="Foto: pinke Orchidee"/>
    <path d="M447,215 C395,255 375,350 382,430 C390,530 420,600 447,632 Z" fill="#fff"/>
    <path d="M447,235 C410,270 398,350 403,430 C410,520 430,590 447,615 Z" fill="url(#sand)" role="img" aria-label="Foto: Zen-Sandgarten"/>
  </svg>
  <div class="brand" style="left:54px;top:258px"><span class="brand-dot"></span><span class="brand-name">Lumawerk</span></div>
  <div class="contact" style="left:53px;top:322px">
    <div>Lumawerk</div><div>8500 Lindenau</div><div>Tel:078 000 12 34</div>
    <div class="gap">info@lumawerk-beratung.ch</div><div class="web">www.lumawerk-beratung.ch</div>
  </div>
</section>

<!-- Inside spread -->
<section class="panel spread inside-spread">
  <svg class="art" viewBox="0 0 895 632">
    <g role="img" aria-label="Foto: Zen-Sandgarten mit pinker Orchidee">
      <path d="M0,0 L290,0 C270,50 200,85 110,95 C60,100 20,110 0,120 Z" fill="url(#sand)"/>
      <ellipse cx="80" cy="45" rx="75" ry="55" fill="url(#bloom)"/>
    </g>
    <path d="M0,120 C40,108 110,98 180,92 C260,85 330,55 390,0 L425,0 C375,90 300,140 200,150 C120,158 50,162 0,168 Z" fill="#fff"/>
    <path d="M470,0 C445,65 405,100 360,122 C425,112 485,65 505,0 Z" fill="#fff"/>
    <path d="M520,0 L800,0 C780,30 770,50 780,70 C830,90 870,130 895,180 L895,200 C860,140 800,102 720,92 C640,82 570,50 520,0 Z" fill="#fff"/>
    <path d="M548,50 C620,32 690,16 738,0 L640,0 C602,20 572,36 548,50 Z" fill="var(--pink)"/>
    <path d="M800,0 L895,0 L895,160 C870,120 830,90 785,70 C770,50 778,25 800,0 Z" fill="url(#bronze)" role="img" aria-label="Foto: Buddha-Statue aus Bronze"/>
    <circle cx="848" cy="422" r="58" fill="url(#blushRound)" stroke="#fff" stroke-width="5" role="img" aria-label="Foto: pinke Orchidee"/>
    <path d="M0,588 C120,570 260,590 372,632 L330,632 C240,604 120,594 0,600 Z" fill="#fff"/>
  </svg>

  <div class="column" style="left:59px;top:151px">
    <p>Wir rennen und tun, wir sind oft so gefangen im Rad des Aktivismus, dass wir ganz vergessen zu sein. Wir sind so beshäftigt damit etwas zu verändern, dass wir dass wir vollkommen vergessen unser Leben zu geniessen und mit liebe zu erfüllen.</p>
    <p class="accent">Annahme – Wertschätzung – Achtung altmodische fast vergessene Worte.</p>
    <p>Doch diese Worte haben eine power. Es sind Worte mit Wurzeln, Worte die einem eine Heimat geben. Eine Heimat in sich selber und eine Heimat im Leben.<br>Eine Heimat die unabhängig von geografischen Orten und äusseren Umständen ist.</p>
    <p>Gegebneheiten akzeptieren. Körperliche ebenso wie Psychische. Wir sind was wir sind - <strong>Menschen mit Stärken und Schwächen.</strong></p>
    <p>Wertschätzen was ist und mit Achtung verändern was möglich und sinnvoll ist. Annehmen und akzeptieren was ist, und so bleiben will wie es ist.</p>
  </div>

  <h2 class="inside-title" style="left:362px;top:98px">Love your life</h2>
  <div class="column" style="left:362px;top:150px">
    <p>Wenn du nicht weißt wo du bist, kannst du auch nicht wissen wo du landest wenn du dich auf den Weg machst. ( Selbst dann wenn du die Himmelsrichtungen erkennst oder eine Karte besitzt) Erst musst du deinen Ausgangsort kennen.</p>
    <p>Wenn du dein Ziel kennst musst du auch wissen wo du jetzt stehst. So kannst du den besten Weg zur Erreichung deines Zieles finden, und die für dich optimale Reiseroute planen.</p>
    <ul class="checklist">
      <li>Was habe ich</li>
      <li>Wo will ich hin</li>
      <li>Warum</li>
      <li>Was trägt es zu meinem Leben bei<br>wenn ich dieses Ziel erreiche</li>
      <li>Worauf verzichte ich wenn ich<br>dieses Ziel erreich</li>
    </ul>
    <p class="closing" style="width:260px">Oft sind wir so damit beschtigt jemand(etwas) zu werden, dass wir ganz vergessen jemand zu sein.</p>
  </div>
</section>

</body>
</html>
```